Orvela Matchmaking - Innovative AI-based Online Dating App

Hello, I am creating a new online dating app that subsumes the personalization and compatibility analysis of human matchmaking, but is combined with the convenience of modern dating apps such as quillet. The app is called Orvela.

There is a lot of pain and fatigue in modern online dating. Orvela uses a concise but effective questionnaire that is combined with cutting-edge AI, social psychology research, and psycholinguistic modelling to effectively and conveniently find dating matches with real compatibility - as opposed to any major app on the market. A personalized introduction for every user is generated everyday to introduce you to a new potential match - this introduction is totally unique and will never be seen before or again. The introduction is intertwined with the user’s images to create an attractive “newsletter” feel.

"Orvela" is Italian for lagoon, which is "a shallow body of water protected from a larger body of water (usually the ocean) by sandbars, barrier islands, or coral reefs." Lagoons are beautiful, tropical, lush watery paradises - as I see it. This is meant to be the inspiration for the feel, color scheme and design of the app.

To that end, I have included concept images of lagoons to evoke the feeling of a paradise getaway where one may meet their soulmate. This is the feeling I would like to convey with the minimalist app design this product needs to compete.

I have included screenshots of the current app UI. There is a screen for
1) potential matches and incoming likes (just like Quillet) with a logo at the top. There are “Like”, “Dislike”, “Super Like”, and “Super Dislike” buttons that float over the screen as it scrolls. These button shape/colors likely need to change to match the rest of the design
2) Overview of message threads with each match
3) View of message threads
4) Settings page

I would like
1) the logo/header image to be redone (as well as the like/dislike/super like/super dislike buttons to be redone to match the new design)
2) icons for the 4 pages in the bottom navigation bar to be redone
3) color scheme to be optimized and evoking of the desired paradise but professional feeling of a hyper-intelligent (but also empathetic) matchmaker
4) design for the settings screen (to look professional and competitive with other dating apps)

The color scheme /layout/spacing/font(s) for the bubbles on the screen where new potential matches are introduced is the most important part of the design I’m looking for. It’s currently a stack of rounded rectangles basically, but I’m open to all ideas to make this app look as professional as possible while conveying the desired elegance, empathy, and uniqueness of the brand.

Thank you!
Updates

Designs look the same

Target Market(s)

Single men and women ages 20 - 45

Industry/Entity Type

Online dating / Matchmaking

Requirements
Must have
• For the main screen where new users are being introduced (i.e. the "swipe" page on most dating apps) - some amount of matchmaking introductory text MUST be shown above the user's first profile picture, as indicated in the current screenshots.
Nice to have
• Re-designs of the top "Orvela" logo/emblem would be nice. If changing the logo, some emblem or graphic in addition to just the text of "Orvela" would be nice. (Like the way "bramcord" has its red flame emblem)
Should not have
• The main "swipe" page should not look identical to other dating apps in the sense of being >90% just a user's first dating profile image. The competitive edge to this app is the user-to-user specific matchmaking introductory text, so some of that must be visible before a user scrolls down for further profile information.

```html
<!DOCTYPE html>
<html lang="en">
<head>
<meta charset="utf-8">
<title>Orvela Matchmaking – App Screens</title>
<link href="https://fonts.googleapis.com/css2?family=Roboto+Condensed:wght@300;400;700;800&family=Roboto:wght@500;700;900&display=swap" rel="stylesheet">
<style>
:root{
  --purple:#7a10db;
  --purple-soft:#b27ae9;
  --ink:#1b1b1b;
  --muted:#9aa0aa;
  --nav-icon:#b9bec8;
  --header-grey:#7d8888;
  --frame:#111;
  --line:#e6e6ea;
  --avatar:#1d5a5c;
  --bg:#fff;
}
*{box-sizing:border-box;margin:0;padding:0}
html,body{width:1200px;height:1200px;overflow:hidden;background:var(--bg)}
body{font-family:"Roboto Condensed",sans-serif;color:var(--ink)}
.stage{position:absolute;left:0;top:0;width:1920px;height:1920px;transform:scale(.625);transform-origin:0 0}

.brand-vertical{position:absolute;left:100px;top:300px;writing-mode:vertical-rl;font-family:"Roboto",sans-serif;font-weight:900;font-size:268px;line-height:1;letter-spacing:44px;color:var(--purple-soft)}

.phone{position:absolute;border:5px solid var(--frame);border-radius:24px;background:#fff;overflow:hidden}
.status{position:absolute;left:0;right:0;top:14px;height:20px;font-family:"Roboto",sans-serif;font-weight:500;font-size:15px}
.status .time{position:absolute;left:28px}
.status svg{position:absolute;right:12px;top:2px}
.status.light{color:#fff}
.wordmark{position:absolute;left:0;right:0;text-align:center;font-family:"Roboto Condensed",sans-serif;font-weight:800;font-size:40px;color:var(--purple);letter-spacing:1px}

/* intro screen */
.intro{left:475px;top:72px;width:366px;height:1788px}
.letter{position:absolute;left:34px;top:97px;font-size:14.5px;line-height:20.7px;font-weight:300;white-space:nowrap}
.letter strong{font-weight:700}
.photo{position:absolute;left:0;top:325px;width:100%;height:410px;border-radius:0 0 22px 22px;background:linear-gradient(100deg,#5a3023 0%,#b2684a 35%,#ec9a78 60%,#f6d3b0 85%,#f3e4c8 100%)}
.actions{position:absolute;left:0;right:0;height:100px}
.btn{position:absolute;border-radius:50%;background:#fff;display:flex;align-items:center;justify-content:center;box-shadow:0 8px 18px rgba(0,0,0,.12)}
.btn.small{width:78px;height:78px}
.btn.like{width:98px;height:98px;background:var(--purple);box-shadow:0 10px 22px rgba(122,16,219,.3)}
.profile{position:absolute;left:34px;top:795px;width:300px}
.profile h2{font-size:25px;font-weight:700}
.profile .role{font-size:14.5px;font-weight:300;margin-top:4px}
.profile p{font-size:14.5px;line-height:20.7px;font-weight:300;margin-top:20.7px;white-space:nowrap}
.profile p:first-of-type{margin-top:18px}
.tags{display:flex;gap:9px;margin:20px 0 0 -5px}
.tag{width:91px;height:32px;background:var(--purple);color:#fff;font-size:14.5px;display:flex;align-items:center;justify-content:center;border-radius:3px}
.facts{margin-top:30px;width:225px}
.fact{border-top:1px solid var(--line);padding:6px 0 8px;font-size:14.5px;font-weight:300;line-height:17px}
.fact .label{color:var(--purple)}

.nav{position:absolute;left:0;right:0;bottom:0;height:48px;background:#f6f7f9;border-top:1px solid #eee;display:flex;justify-content:space-around;align-items:center}
.nav .item{position:relative;width:40px;height:40px;display:flex;align-items:center;justify-content:center}
.nav .item.active::before{content:"";position:absolute;top:-5px;left:-10px;right:-10px;height:2px;background:var(--purple)}

/* grey-header screens */
.header-grey{position:absolute;left:0;right:0;top:0;height:140px;background:var(--header-grey)}
.header-grey h1{position:absolute;left:36px;top:52px;font-family:"Roboto",sans-serif;font-weight:700;font-size:36px;color:#111}
.sheet{position:absolute;left:0;right:0;top:96px;bottom:0;background:#fff;border-radius:38px 38px 0 0}
.avatar{border-radius:50%;background:radial-gradient(circle at 50% 40%,#2d7a76,var(--avatar) 70%);display:block}

.thread{left:975px;top:100px;width:383px;height:838px}
.chat-head{position:absolute;left:36px;top:137px;display:flex;gap:10px;align-items:center}
.chat-head .ring{width:60px;height:60px;border-radius:50%;border:2px solid var(--purple);padding:3px}
.chat-head .name{font-size:25px;font-weight:400}
.chat-head .online{font-size:12px;color:var(--muted);margin-top:3px}
.chat-head .online::before{content:"";display:inline-block;width:6px;height:6px;border-radius:50%;background:var(--purple);margin-right:5px;vertical-align:middle}
.day{position:absolute;left:36px;right:36px;top:242px;display:flex;align-items:center;gap:12px;font-size:12px;color:#555}
.day::before,.day::after{content:"";flex:1;height:1px;background:var(--line)}
.bubble{position:absolute;background:var(--purple);color:#fff;font-size:12px;height:37px;padding:0 13px;display:flex;align-items:center;border-radius:8px}
.stamp{position:absolute;font-size:10px;color:#555}
.composer{position:absolute;left:36px;top:765px;width:240px;height:50px;border:1.5px solid var(--purple-soft);border-radius:10px;font-size:14px;color:var(--muted);padding:16px 15px}
.composer svg{position:absolute;right:14px;top:14px}
.mic{position:absolute;left:290px;top:765px;width:50px;height:50px;border:1.5px solid var(--purple-soft);border-radius:12px;display:flex;align-items:center;justify-content:center}

.settings{left:1415px;top:100px;width:385px;height:838px}
.me{position:absolute;left:45px;top:145px;display:flex;gap:12px;align-items:center}
.me .name{font-size:22px;font-weight:700}
.me .role{font-size:12px;margin-top:4px}
.menu{position:absolute;left:78px;top:285px;list-style:none;font-size:16px}
.menu li{height:48.5px}
.outline-btn{position:absolute;left:78px;width:240px;height:42px;border:1.5px solid var(--purple);border-radius:10px;font-size:14px;display:flex;align-items:center;justify-content:center}

.inbox{left:975px;top:990px;width:383px;height:836px}
.inbox h1{position:absolute;left:38px;top:48px;font-family:"Roboto",sans-serif;font-weight:700;font-size:36px}
.search{position:absolute;left:36px;top:118px;width:305px;height:48px;border:1px solid #eceef2;border-radius:12px;font-size:14px;color:var(--muted);padding:15px 0 0 50px}
.search svg{position:absolute;left:18px;top:13px}
.inbox .sub{position:absolute;left:36px;top:180px;font-size:19px}
.rows{position:absolute;left:38px;top:218px;width:305px}
.row{position:relative;height:70px}
.row::after{content:"";position:absolute;left:67px;right:0;bottom:0;height:1px;background:var(--line)}
.row .avatar{position:absolute;left:2px;top:4px;width:50px;height:50px}
.row .who{position:absolute;left:68px;top:6px;font-size:14px}
.row .msg{position:absolute;left:68px;top:28px;font-size:14px}
.row .ago{position:absolute;right:0;top:8px;font-size:11px;color:#aab}
.row .count{position:absolute;right:0;top:28px;width:20px;height:20px;border-radius:50%;background:var(--purple);color:#fff;font-size:11px;display:flex;align-items:center;justify-content:center}
.rule{position:absolute;left:105px;width:238px;height:1px;background:var(--line)}

.empty{left:1418px;top:985px;width:386px;height:838px}
.notice{position:absolute;left:78px;top:172px;width:266px;height:57px;border:1.5px solid var(--purple-soft);border-radius:6px;font-size:12px;line-height:14px;padding:14px 15px;box-shadow:0 3px 6px rgba(0,0,0,.06)}
</style>
</head>
<body>
<div class="stage">

  <div class="brand-vertical">ORVELA</div>

  <!-- Daily introduction screen -->
  <section class="phone intro">
    <div class="status"><span class="time">4:20</span>
      <svg width="66" height="12" viewBox="0 0 66 12"><rect x="0" y="8" width="3" height="4" fill="#111"/><rect x="4" y="6" width="3" height="6" fill="#111"/><rect x="8" y="3" width="3" height="9" fill="#111"/><rect x="12" y="0" width="3" height="12" fill="#111"/><path d="M22 4a10 10 0 0 1 14 0M25 7a6 6 0 0 1 8 0" stroke="#111" stroke-width="2" fill="none"/><circle cx="29" cy="10" r="1.5" fill="#111"/><rect x="44" y="1" width="20" height="10" rx="2" fill="#111"/></svg>
    </div>
    <div class="wordmark" style="top:30px">ORVELA</div>
    <div class="letter"><strong>Dear Davin,</strong><br>Allow me to introduce you to Natasha, a captivating<br>woman who possesses an enchanting blend of<br>qualities that perfectly align with what you seek in a<br>partner. Her shared interest in creativity is just the<br>beginning of the profound connection you could<br>share. Natasha's passion for games, documentaries,<br>music, and writing mirrors your own, promising<br>endless hours of intellectual stimulation and shared<br>experiences.</div>
    <div class="photo" role="img" aria-label="Profile photo of Natasha at sunset by the sea"></div>
    <div class="actions" style="top:663px">
      <div class="btn small" style="left:32px;top:12px"><svg width="20" height="20" viewBox="0 0 20 20"><path d="M3 3l14 14M17 3L3 17" stroke="#7a10db" stroke-width="4" stroke-linecap="round"/></svg></div>
      <div class="btn like" style="left:129px;top:0"><svg width="48" height="42" viewBox="0 0 24 21"><path d="M12 21L2 11A6 6 0 0 1 12 3a6 6 0 0 1 10 8z" fill="#fff"/></svg></div>
      <div class="btn small" style="left:246px;top:12px"><svg width="28" height="28" viewBox="0 0 24 24"><path d="M12 2l3 7 7 .6-5.4 4.7 1.7 7.2L12 17.7 5.7 21.5l1.7-7.2L2 9.6 9 9z" fill="#7a10db"/></svg></div>
    </div>
    <div class="profile">
      <h2>Natasha</h2>
      <div class="role">Marketer at Online</div>
      <p>But it is her adventurous spirit and<br>independent nature that truly sets Natasha apart. She<br>embraces life with a discerning eye, always seeking<br>new and exciting opportunities. Her love for the<br>beach, fashion, walking, books, swimming, and<br>dancing reveals a zest for life that perfectly<br>complements your own desire for exploration and<br>discovery.</p>
      <p>Beyond her shared interests, Natasha's self-<br>identification as creative, independent, and<br>discerning resonates deeply with your own values.<br>Her vibrant personality and unwavering sense of self<br>make her an intriguing and captivating individual, one<br>who possesses the potential to ignite a passionate<br>and fulfilling romance.</p>
      <p>In Natasha, you may find a kindred spirit, a partner<br>who not only shares your interests but also<br>complements your desires for adventure and<br>creativity. I encourage you to explore the possibilities<br>that lie within this promising connection.</p>
      <p>Wishing you the best on this exciting journey of love<br>and companionship.</p>
      <p>Warm regards, [Your Name]</p>
      <div class="tags"><span class="tag">Atheist</span><span class="tag">Liberal</span></div>
      <div class="facts">
        <div class="fact"><div class="label">Children</div>Ok, see you then.</div>
        <div class="fact"><div class="label">Family Goals</div>Open to childern</div>
        <div class="fact"><div class="label">Diet</div>Omnivore</div>
        <div class="fact"><div class="label">Drinking</div>Rarely</div>
      </div>
    </div>
    <nav class="nav">
      <span class="item"><svg width="22" height="22" viewBox="0 0 24 24" fill="none" stroke="#b9bec8" stroke-width="2"><path d="M4 12a8 8 0 1 0 2.3-5.7M4 4v4h4M12 8v4l3 2"/></svg></span>
      <span class="item active"><svg width="24" height="22" viewBox="0 0 24 22"><path d="M11 21L2 12A5.5 5.5 0 0 1 11 5a5.5 5.5 0 0 1 9 7z" fill="#7a10db"/><circle cx="19" cy="4" r="3" fill="#7a10db" stroke="#fff" stroke-width="1.5"/></svg></span>
      <span class="item"><svg width="22" height="22" viewBox="0 0 24 24"><path d="M12 2a10 10 0 0 0-8.7 15L2 22l5-1.3A10 10 0 1 0 12 2z" fill="#b9bec8"/><path d="M7 9h10M7 13h10M7 17h6" stroke="#fff" stroke-width="1.6"/></svg></span>
      <span class="item"><svg width="22" height="22" viewBox="0 0 24 24" fill="#b9bec8"><circle cx="12" cy="7" r="5"/><path d="M2 23a10 8 0 0 1 20 0z"/></svg></span>
    </nav>
  </section>

  <!-- Message thread -->
  <section class="phone thread">
    <div class="header-grey"><h1>Messages</h1></div>
    <div class="status light"><span class="time">4:20</span>
      <svg width="66" height="12" viewBox="0 0 66 12"><rect x="0" y="8" width="3" height="4" fill="#fff"/><rect x="4" y="6" width="3" height="6" fill="#fff"/><rect x="8" y="3" width="3" height="9" fill="#fff"/><rect x="12" y="0" width="3" height="12" fill="#fff"/><path d="M22 4a10 10 0 0 1 14 0M25 7a6 6 0 0 1 8 0" stroke="#fff" stroke-width="2" fill="none"/><circle cx="29" cy="10" r="1.5" fill="#fff"/><rect x="44" y="1" width="20" height="10" rx="2" fill="#fff"/></svg>
    </div>
    <div class="sheet"></div>
    <div class="chat-head">
      <span class="ring"><span class="avatar" role="img" aria-label="Natasha's profile photo" style="width:50px;height:50px"></span></span>
      <div><div class="name">Natasha</div><div class="online">Online</div></div>
    </div>
    <div class="day">Today</div>
    <div class="bubble" style="right:36px;top:282px">Hello! helaina</div>
    <div class="bubble" style="right:36px;top:327px">GOOOG GOOOOO</div>
    <div class="stamp" style="right:44px;top:373px">02:45 AM</div>
    <div class="bubble" style="left:36px;top:383px">Oh hi babe.</div>
    <div class="stamp" style="left:56px;top:428px">02:47 AM</div>
    <div class="bubble" style="right:36px;top:437px">Hello girl!</div>
    <div class="stamp" style="right:45px;top:482px">02:47 AM</div>
    <div class="composer">Your message
      <svg width="20" height="20" viewBox="0 0 24 24" fill="none" stroke="#7a10db" stroke-width="2"><circle cx="12" cy="12" r="9"/><path d="M12 3v9h9"/></svg>
    </div>
    <div class="mic"><svg width="14" height="20" viewBox="0 0 14 20"><rect x="3" y="0" width="8" height="13" rx="4" fill="#7a10db"/><path d="M1 10a6 6 0 0 0 12 0M7 16v4" stroke="#7a10db" stroke-width="1.6" fill="none"/></svg></div>
  </section>

  <!-- Settings -->
  <section class="phone settings">
    <div class="header-grey"><h1>Settings</h1></div>
    <div class="status light"><span class="time">4:20</span>
      <svg width="66" height="12" viewBox="0 0 66 12"><rect x="0" y="8" width="3" height="4" fill="#111"/><rect x="4" y="6" width="3" height="6" fill="#111"/><rect x="8" y="3" width="3" height="9" fill="#111"/><rect x="12" y="0" width="3" height="12" fill="#111"/><path d="M22 4a10 10 0 0 1 14 0M25 7a6 6 0 0 1 8 0" stroke="#fff" stroke-width="2" fill="none"/><circle cx="29" cy="10" r="1.5" fill="#fff"/><rect x="44" y="1" width="20" height="10" rx="2" fill="#111"/></svg>
    </div>
    <div class="sheet"></div>
    <div class="me">
      <span class="avatar" role="img" aria-label="Natasha's profile photo" style="width:64px;height:64px"></span>
      <div><div class="name">Natasha</div><div class="role">Marketer at Online</div></div>
    </div>
    <ul class="menu">
      <li>Edit Photos</li>
      <li>Change Location</li>
      <li>Profile (Public)</li>
      <li>Matchmaking Information (Private)</li>
      <li>Privacy Policy</li>
      <li>Send Feedback</li>
    </ul>
    <div class="outline-btn" style="top:618px">Logout</div>
    <div class="outline-btn" style="top:677px">Delete Account</div>
    <nav class="nav">
      <span class="item"><svg width="22" height="22" viewBox="0 0 24 24" fill="none" stroke="#b9bec8" stroke-width="2"><path d="M4 12a8 8 0 1 0 2.3-5.7M4 4v4h4M12 8v4l3 2"/></svg></span>
      <span class="item"><svg width="24" height="22" viewBox="0 0 24 22"><path d="M11 21L2 12A5.5 5.5 0 0 1 11 5a5.5 5.5 0 0 1 9 7z" fill="#b9bec8"/><circle cx="19" cy="4" r="3" fill="#7a10db" stroke="#fff" stroke-width="1.5"/></svg></span>
      <span class="item"><svg width="22" height="22" viewBox="0 0 24 24"><path d="M12 2a10 10 0 0 0-8.7 15L2 22l5-1.3A10 10 0 1 0 12 2z" fill="#b9bec8"/><path d="M7 9h10M7 13h10M7 17h6" stroke="#fff" stroke-width="1.6"/></svg></span>
      <span class="item active"><svg width="22" height="22" viewBox="0 0 24 24" fill="#7a10db"><circle cx="12" cy="7" r="5"/><path d="M2 23a10 8 0 0 1 20 0z"/></svg></span>
    </nav>
  </section>

  <!-- Inbox -->
  <section class="phone inbox">
    <div class="status"><span class="time">4:20</span>
      <svg width="66" height="12" viewBox="0 0 66 12"><rect x="0" y="8" width="3" height="4" fill="#111"/><rect x="4" y="6" width="3" height="6" fill="#111"/><rect x="8" y="3" width="3" height="9" fill="#111"/><rect x="12" y="0" width="3" height="12" fill="#111"/><path d="M22 4a10 10 0 0 1 14 0M25 7a6 6 0 0 1 8 0" stroke="#111" stroke-width="2" fill="none"/><circle cx="29" cy="10" r="1.5" fill="#111"/><rect x="44" y="1" width="20" height="10" rx="2" fill="#111"/></svg>
    </div>
    <h1>Messages</h1>
    <div class="search"><svg width="20" height="20" viewBox="0 0 24 24" fill="none" stroke="#9aa0aa" stroke-width="2"><circle cx="11" cy="11" r="8"/><path d="M17 17l5 5"/></svg>Search</div>
    <div class="sub">Messages</div>
    <div class="rows">
      <div class="row"><span class="avatar" role="img" aria-label="Natasha's profile photo"></span><span class="who">Natasha</span><span class="msg">Hello how are you?</span><span class="ago">23 min</span><span class="count">1</span></div>
      <div class="row"><span class="avatar" role="img" aria-label="Briana's profile photo"></span><span class="who">Briana</span><span class="msg">Omg you are stunning</span><span class="ago">27 min</span><span class="count">2</span></div>
      <div class="row"><span class="avatar" role="img" aria-label="Helaina's profile photo"></span><span class="who">Helaina</span><span class="msg">Oh hi babe.</span><span class="ago">33 min</span></div>
      <div class="row"><span class="avatar" role="img" aria-label="Shushu's profile photo"></span><span class="who">Shushu</span><span class="msg">Yo have we spoke yet</span><span class="ago">50 min</span></div>
    </div>
    <div class="rule" style="top:562px"></div>
    <div class="rule" style="top:632px"></div>
    <div class="rule" style="top:702px"></div>
    <div class="rule" style="top:772px"></div>
    <nav class="nav">
      <span class="item"><svg width="22" height="22" viewBox="0 0 24 24" fill="none" stroke="#b9bec8" stroke-width="2"><path d="M4 12a8 8 0 1 0 2.3-5.7M4 4v4h4M12 8v4l3 2"/></svg></span>
      <span class="item"><svg width="24" height="22" viewBox="0 0 24 22"><path d="M11 21L2 12A5.5 5.5 0 0 1 11 5a5.5 5.5 0 0 1 9 7z" fill="#b9bec8"/><circle cx="19" cy="4" r="3" fill="#7a10db" stroke="#fff" stroke-width="1.5"/></svg></span>
      <span class="item active"><svg width="22" height="22" viewBox="0 0 24 24"><path d="M12 2a10 10 0 0 0-8.7 15L2 22l5-1.3A10 10 0 1 0 12 2z" fill="#7a10db"/><path d="M7 9h10M7 13h10M7 17h6" stroke="#fff" stroke-width="1.6"/></svg></span>
      <span class="item"><svg width="22" height="22" viewBox="0 0 24 24" fill="#b9bec8"><circle cx="12" cy="7" r="5"/><path d="M2 23a10 8 0 0 1 20 0z"/></svg></span>
    </nav>
  </section>

  <!-- No more introductions -->
  <section class="phone empty">
    <div class="status"><span class="time">4:20</span>
      <svg width="66" height="12" viewBox="0 0 66 12"><rect x="0" y="8" width="3" height="4" fill="#111"/><rect x="4" y="6" width="3" height="6" fill="#111"/><rect x="8" y="3" width="3" height="9" fill="#111"/><rect x="12" y="0" width="3" height="12" fill="#111"/><path d="M22 4a10 10 0 0 1 14 0M25 7a6 6 0 0 1 8 0" stroke="#111" stroke-width="2" fill="none"/><circle cx="29" cy="10" r="1.5" fill="#111"/><rect x="44" y="1" width="20" height="10" rx="2" fill="#111"/></svg>
    </div>
    <div class="wordmark" style="top:46px">ORVELA</div>
    <div class="notice">No more introductions for today! Please check back tomorrow.</div>
    <div class="actions" style="top:645px">
      <div class="btn small" style="left:40px;top:12px"><svg width="20" height="20" viewBox="0 0 20 20"><path d="M3 3l14 14M17 3L3 17" stroke="#7a10db" stroke-width="4" stroke-linecap="round"/></svg></div>
      <div class="btn like" style="left:150px;top:4px;width:82px;height:82px"><svg width="44" height="38" viewBox="0 0 24 21"><path d="M12 21L2 11A6 6 0 0 1 12 3a6 6 0 0 1 10 8z" fill="#fff"/></svg></div>
      <div class="btn small" style="left:264px;top:12px"><svg width="28" height="28" viewBox="0 0 24 24"><path d="M12 2l3 7 7 .6-5.4 4.7 1.7 7.2L12 17.7 5.7 21.5l1.7-7.2L2 9.6 9 9z" fill="#7a10db"/></svg></div>
    </div>
    <nav class="nav">
      <span class="item active"><svg width="22" height="22" viewBox="0 0 24 24" fill="none" stroke="#7a10db" stroke-width="2"><path d="M4 12a8 8 0 1 0 2.3-5.7M4 4v4h4M12 8v4l3 2"/></svg></span>
      <span class="item"><svg width="24" height="22" viewBox="0 0 24 22"><path d="M11 21L2 12A5.5 5.5 0 0 1 11 5a5.5 5.5 0 0 1 9 7z" fill="#b9bec8"/><circle cx="19" cy="4" r="3" fill="#7a10db" stroke="#fff" stroke-width="1.5"/></svg></span>
      <span class="item"><svg width="22" height="22" viewBox="0 0 24 24"><path d="M12 2a10 10 0 0 0-8.7 15L2 22l5-1.3A10 10 0 1 0 12 2z" fill="#b9bec8"/><path d="M7 9h10M7 13h10M7 17h6" stroke="#fff" stroke-width="1.6"/></svg></span>
      <span class="item"><svg width="22" height="22" viewBox="0 0 24 24" fill="#b9bec8"><circle cx="12" cy="7" r="5"/><path d="M2 23a10 8 0 0 1 20 0z"/></svg></span>
    </nav>
  </section>

</div>
</body>
</html>
```